Business Card Design Project

Use newly designed logo and tie into newly designed website
I need a new logo and website layout designed for my partner's business. This is a birthday present. His business is interior painting, wallpapering and design. He also has access to a wide variety of products including carpet, fabrics, furniture, wallpaper, tile, countertops, etc. I have attached some screen shots of his website for reference. He is a one man shop and has a stellar reputation with his customers. He is on-time, very tidy, excellent with animals, and always finishes on time and on budget. There are no restrictions on colors or fonts. The logo needs to work well with the website, business cards and printed materials. The website needs to flow content for device size so it looks just as good on a cell phone or tablet as it does on a desktop computer. Whatever the heck that's called!Thanks. I am looking forward to seeing everyone's ideas.
Updates
Hi Designers,
We've reopened this project as our logo design project has just completed.
Please refer to the uploaded files and make use of either Horizontal or Vertical versions of the logo depending on what you think is suitable for your design proposals.
We look forward to your creative submissions!
Target Market(s)
Consumers looking to improve the interior environment of their homes by updating wall paint or paper, flooring (either carpet, tile, or hardwoods), counter tops, window treatments, etc. Clients tend to be more upper middle class and have certain taste levels and expectations. New logo, website and business card should align to meet those levels.
Industry/Entity Type
Cell Phone
Look and feel
Each slider illustrates characteristics of the customer's brand and the style your logo design should communicate.

```html
<!DOCTYPE html>
<html lang="en">
<head>
<meta charset="utf-8">
<title>Bellandi Interior Designs – Business Card</title>
<link rel="stylesheet" href="https://fonts.googleapis.com/css2?family=Open+Sans:wght@400;600&display=swap">
<style>
  :root {
    --page: #ffffff;
    --card-dark: #232323;
    --card-mid: #2e2e2e;
    --gold: #bfa670;
    --gold-soft: #a8946a;
    --purple: #2b2352;
    --text-gold: #cdb98a;
  }
  * { box-sizing: border-box; margin: 0; padding: 0; }
  html, body {
    width: 1200px; height: 900px; overflow: hidden;
    background: var(--page);
    font-family: "Open Sans", sans-serif;
  }
  .stage {
    width: 1200px; height: 900px;
    display: flex; align-items: center; justify-content: center;
  }
  .card {
    position: relative;
    width: 900px; height: 540px;
    border-radius: 34px;
    overflow: hidden;
  }
  .card__texture {
    position: absolute; inset: 0;
    background: radial-gradient(ellipse at 50% 40%, var(--card-mid), var(--card-dark) 75%);
  }
  .card__frame { position: absolute; inset: 0; }
  .brand {
    position: absolute; left: 52px; top: 34px; width: 590px;
  }
  .brand__rule {
    height: 2px; background: var(--gold-soft); margin-left: 50px; width: 490px;
  }
  .brand__rule--inner { margin: 6px 0 0 0; width: 540px; height: 1px; }
  .brand__rule--bottom { margin: 10px 0 6px 0; width: 590px; height: 1px; }
  .brand__row {
    display: flex; align-items: center; gap: 22px; margin-top: 16px;
  }
  .brand__square {
    width: 120px; height: 120px; background: var(--gold);
    flex: none;
  }
  .brand__name {
    color: var(--gold);
    font-weight: 600;
    font-size: 54px;
    line-height: 1.05;
    letter-spacing: 2px;
    text-transform: uppercase;
  }
  .brand__name span { display: block; font-size: 33px; letter-spacing: 1.5px; }
  .person {
    position: absolute; left: 56px; top: 318px;
  }
  .person__name {
    color: var(--purple); font-size: 30px; font-weight: 400; line-height: 1.1;
  }
  .person__role {
    color: var(--text-gold); font-size: 16px; margin-top: 6px;
  }
  .contacts {
    position: absolute; left: 56px; top: 400px; list-style: none;
  }
  .contacts__item {
    display: flex; align-items: center; gap: 12px;
    color: var(--text-gold); font-size: 23px; line-height: 30px;
  }
  .contacts__icon { width: 20px; height: 20px; fill: var(--purple); flex: none; }
</style>
</head>
<body>
<main class="stage">
  <article class="card">
    <div class="card__texture" role="img" aria-label="Faint pattern of furniture and window silhouettes on charcoal"></div>

    <svg class="card__frame" width="900" height="540" viewBox="0 0 900 540" aria-hidden="true">
      <rect x="3" y="3" width="894" height="534" rx="32" fill="none" stroke="var(--gold)" stroke-width="3"/>
      <rect x="9" y="9" width="882" height="522" rx="27" fill="none" stroke="var(--purple)" stroke-width="4"/>
      <rect x="15" y="15" width="870" height="510" rx="22" fill="none" stroke="var(--gold)" stroke-width="2"/>
    </svg>

    <header class="brand">
      <div class="brand__rule"></div>
      <div class="brand__rule brand__rule--inner"></div>
      <div class="brand__row">
        <div class="brand__square"></div>
        <h1 class="brand__name">Bellandi<span>Interior Designs</span></h1>
      </div>
      <div class="brand__rule brand__rule--bottom"></div>
      <div class="brand__rule"></div>
    </header>

    <section class="person">
      <h2 class="person__name">Ansel Rowe</h2>
      <p class="person__role">Manager</p>
    </section>

    <ul class="contacts">
      <li class="contacts__item">
        <svg class="contacts__icon" viewBox="0 0 24 24"><path d="M6.6 10.8a15.1 15.1 0 0 0 6.6 6.6l2.2-2.2c.3-.3.7-.4 1-.2 1.1.4 2.3.6 3.6.6.6 0 1 .4 1 1V20c0 .6-.4 1-1 1A17 17 0 0 1 3 4c0-.6.4-1 1-1h3.5c.6 0 1 .4 1 1 0 1.3.2 2.5.6 3.6.1.3 0 .7-.2 1z"/></svg>
        154-555-0137
      </li>
      <li class="contacts__item">
        <svg class="contacts__icon" viewBox="0 0 24 24"><path d="M12 2a10 10 0 1 0 0 20 10 10 0 0 0 0-20zm6.9 6h-3a15.7 15.7 0 0 0-1.3-3.9A8 8 0 0 1 18.9 8zM12 4c.8 1.2 1.5 2.5 1.9 4h-3.8c.4-1.5 1.1-2.8 1.9-4zM4.3 14a8 8 0 0 1 0-4h3.4a16 16 0 0 0 0 4zm.8 2h3a15.7 15.7 0 0 0 1.3 3.9A8 8 0 0 1 5.1 16zm3-8h-3a8 8 0 0 1 4.3-3.9C8.9 5.3 8.4 6.6 8.1 8zM12 20c-.8-1.2-1.5-2.5-1.9-4h3.8c-.4 1.5-1.1 2.8-1.9 4zm2.3-6H9.7a14.7 14.7 0 0 1 0-4h4.6a14.7 14.7 0 0 1 0 4zm.3 5.9c.6-1.2 1-2.5 1.3-3.9h3a8 8 0 0 1-4.3 3.9zm1.7-5.9a16 16 0 0 0 0-4h3.4a8 8 0 0 1 0 4z"/></svg>
        www.bellandidesigns.com
      </li>
      <li class="contacts__item">
        <svg class="contacts__icon" viewBox="0 0 24 24"><path d="M3 5h18c.6 0 1 .4 1 1v12c0 .6-.4 1-1 1H3c-.6 0-1-.4-1-1V6c0-.6.4-1 1-1zm9 7.5L4 7.3V17h16V7.3z"/></svg>
        info@www.bellandidesigns.com
      </li>
      <li class="contacts__item">
        <svg class="contacts__icon" viewBox="0 0 24 24"><path d="M12 3 2 12h3v8h5v-6h4v6h5v-8h3z"/></svg>
        48 Millbrook Rd. Ashford, NJ. 08610
      </li>
    </ul>
  </article>
</main>
</body>
</html>
```